Re design current site.

Redesign of the current site. Like current design But I don't own it so I need a custom design similar to the current one. Want the model pictures to be shown off as they currently do on the home page I want to show off contact info make it very noticeable and readable.
Target Market(s)
Males age 30-60
Number of Pages Required
1 page
Requirements
Must have
- Must show off model pictures on the page. Must show contact info easy to read easy to find.

```html
<!DOCTYPE html>
<html lang="en">
<head>
<meta charset="utf-8">
<title>Veranda Models</title>
<link rel="stylesheet" href="https://fonts.googleapis.com/css2?family=Jost:wght@300;400;500&display=swap">
<style>
:root{
  --red:#cf1f2a;
  --dark:#1d1d1d;
  --ink:#222;
  --grey:#6b6b6b;
  --light:#f2f0f0;
  --white:#fff;
}
*{margin:0;padding:0;box-sizing:border-box}
html,body{width:1200px;height:2628px;overflow:hidden}
body{position:relative;font-family:"Jost",Arial,sans-serif;color:var(--ink);background:var(--white)}
.abs{position:absolute}
/* header */
.topbar{left:0;top:0;width:1200px;height:140px;background:var(--dark)}
.brand{left:100px;top:56px;display:flex;align-items:center;gap:14px}
.brand-mark{width:36px;height:36px;background:var(--white)}
.brand-name{font-size:36px;font-weight:400;color:var(--white);letter-spacing:1px;line-height:1}
.call{left:586px;top:44px;display:flex;align-items:center;gap:12px}
.call-label{font-size:13px;color:#9a9a9a;letter-spacing:1px;line-height:1}
.call-number{font-size:34px;font-weight:300;color:var(--white);line-height:1.1}
.book-btn{left:941px;top:58px;width:159px;height:40px;background:var(--white);color:var(--ink);font-size:16px;display:flex;align-items:center;justify-content:center;letter-spacing:.5px}
.mainnav{left:0;top:140px;width:1200px;height:53px;background:var(--red);display:flex;justify-content:center;align-items:center;gap:0}
.mainnav span{color:var(--white);font-size:16px;letter-spacing:1.2px;position:absolute;transform:translateX(-50%)}
/* hero */
.hero{left:0;top:193px;width:1200px;height:562px;background:linear-gradient(180deg,#e8e5d8 0%,#dcd8c8 45%,#8c8f8c 62%,#a9a79e 100%)}
.hero-figure{left:560px;top:193px;width:560px;height:562px;background:linear-gradient(180deg,#c8a48c 0%,#b98c74 55%,#a98470 100%);opacity:.55}
.hero-title{left:150px;top:280px;font-size:84px;font-weight:300;line-height:1.05;color:#1c1c1c;text-align:center;width:330px}
.hero-sub{left:100px;top:492px;width:430px;text-align:center;font-size:22px;font-weight:300;color:#333;line-height:1.4}
.dots{display:flex;gap:8px}
.dot{width:9px;height:9px;border-radius:50%;border:1.5px solid var(--white)}
.dot.on{background:var(--white)}
/* welcome */
.section-title{width:1200px;left:0;text-align:center;font-weight:300;line-height:1}
.welcome-title{top:800px;font-size:33px;color:var(--red)}
.rule{height:1px;background:#ddd}
.welcome-text{left:120px;top:878px;width:960px;text-align:center;font-size:14px;line-height:23px;color:var(--grey)}
.arrow-btn{width:23px;height:23px;border:1px solid #bbb;display:flex;align-items:center;justify-content:center}
.model-photo{top:979px;width:316px;height:209px}
.model-name{top:1202px;width:316px;text-align:center;font-size:21px;color:var(--ink);line-height:1}
.model-stats{top:1230px;width:316px;text-align:center;font-size:13px;color:var(--grey)}
/* testimonials */
.testimonials{left:0;top:1323px;width:1200px;height:427px;background:var(--light)}
.testi-title{top:1368px;font-size:35px;color:#1c1c1c}
.quote-mark{font-family:Georgia,serif;font-size:64px;color:#c9c9c9;line-height:1}
.testi-text{left:236px;top:1441px;width:728px;text-align:center;font-size:15px;line-height:22px;color:var(--grey)}
.avatar{left:554px;top:1544px;width:84px;height:84px;border-radius:50%;border:3px solid var(--white);background:linear-gradient(160deg,#8fb7cf,#b88f76)}
.testi-name{left:0;top:1641px;width:1200px;text-align:center;font-size:14px;color:var(--red);letter-spacing:.3px}
.rdot{width:10px;height:10px;border-radius:50%;border:1.5px solid var(--red)}
.rdot.on{background:var(--red)}
/* video */
.video-title{top:1795px;font-size:35px;color:#1c1c1c}
.video-text{left:100px;top:1884px;width:522px;font-size:13.5px;line-height:26px;color:var(--grey)}
.video-text p+p{margin-top:4px}
.more-btn{left:100px;top:2111px;width:233px;height:48px;border:1px solid var(--red);color:var(--red);font-size:17px;letter-spacing:.8px;display:flex;align-items:center;justify-content:center;gap:10px}
.video-frame{left:667px;top:1883px;width:435px;height:276px;border:1px solid #ccc;background:var(--white);padding:10px}
.video-still{width:413px;height:254px;background:linear-gradient(180deg,#cfd6d6 0%,#b7c4c8 40%,#d8c9b4 60%,#cbb59a 100%);position:relative}
.video-bar{position:absolute;left:0;bottom:0;width:100%;height:28px;background:#2a2a2a}
/* footer */
.footer{left:0;top:2234px;width:1200px;height:308px;background:var(--red);color:var(--white)}
.foot-head{font-size:22px;font-weight:400;color:var(--white)}
.foot-link{font-size:16px;color:#f6d6d8;line-height:29px}
.foot-divider{width:1px;height:220px;background:rgba(255,255,255,.18)}
.foot-contact{font-size:16px;color:#f6d6d8;line-height:28px}
.foot-strong{font-size:17px;color:var(--white);display:flex;align-items:center;gap:10px;line-height:29px}
.signup{left:788px;top:2330px;width:312px;height:39px;background:var(--white);display:flex;align-items:center;justify-content:space-between;padding:0 5px 0 12px}
.signup-field{font-size:13px;color:#aaa;letter-spacing:.8px}
.signup-btn{background:var(--red);color:var(--white);font-size:12px;font-weight:500;letter-spacing:.6px;padding:6px 10px}
.social{width:34px;height:34px;border-radius:50%;background:rgba(255,255,255,.35)}
.bottombar{left:0;top:2542px;width:1200px;height:86px;background:var(--dark);color:#bdbdbd;font-size:12px;display:flex;align-items:center;justify-content:center}
</style>
</head>
<body>

<header class="abs topbar"></header>
<div class="abs brand"><span class="brand-mark"></span><span class="brand-name">VERANDA MODELS</span></div>
<div class="abs call">
  <svg width="32" height="32" viewBox="0 0 32 32" aria-hidden="true"><circle cx="16" cy="16" r="15" fill="none" stroke="#6a6a6a" stroke-width="2"/><path d="M11 9.5c1-.8 2-.5 2.6.5l1.2 2c.4.8.2 1.6-.5 2.1l-.8.6c.6 1.6 1.9 3 3.6 3.7l.6-.8c.5-.7 1.4-.9 2.1-.5l2 1.2c1 .6 1.2 1.7.4 2.6-1.2 1.4-3 1.7-4.8.9-3.3-1.5-5.8-4-7.2-7.3-.7-1.8-.4-3.6.8-5z" fill="#6a6a6a"/></svg>
  <div><div class="call-label">CALL US TODAY:</div><div class="call-number">555-014-2876</div></div>
</div>
<div class="abs book-btn">BOOK NOW!</div>

<nav class="abs mainnav">
  <span style="left:240px">HOME</span>
  <span style="left:382px">BOOKINGS</span>
  <span style="left:523px">RATES</span>
  <span style="left:652px">MODELS</span>
  <span style="left:811px">EMPLOYMENT</span>
  <span style="left:961px">LINKS</span>
</nav>

<section>
  <div class="abs hero" role="img" aria-label="Beach scene with a model in swimwear by the sea"></div>
  <div class="abs hero-figure" role="img" aria-label="Model posing on the right of the banner"></div>
  <h1 class="abs hero-title">Veranda Models</h1>
  <p class="abs hero-sub">VerandaModels Escorts Agency that offers the best companionship &nbsp;in the Miami</p>
  <div class="abs dots" style="left:294px;top:700px"><span class="dot on"></span><span class="dot"></span><span class="dot on"></span></div>
</section>

<section>
  <h2 class="abs section-title welcome-title">WELCOME TO VERANDAMODELS</h2>
  <div class="abs rule" style="left:100px;top:850px;width:1000px"></div>
  <p class="abs welcome-text">VerandaModels Concierge Service allows clients to request VerandaModels to search for models in the location you plan on traveling to. We will search and find attractive models for the dates requested. We also verify they are interested in the service you expect/request and that the pictures we have are recent and real.</p>
  <div class="abs arrow-btn" style="left:1045px;top:941px"><svg width="8" height="12" viewBox="0 0 8 12"><path d="M6 1L2 6l4 5" fill="none" stroke="#777" stroke-width="1.5"/></svg></div>
  <div class="abs arrow-btn" style="left:1076px;top:941px"><svg width="8" height="12" viewBox="0 0 8 12"><path d="M2 1l4 5-4 5" fill="none" stroke="#777" stroke-width="1.5"/></svg></div>

  <div class="abs model-photo" style="left:100px;background:linear-gradient(180deg,#f3ebe8,#e7dcd8)" role="img" aria-label="Model portrait in a knit dress"></div>
  <div class="abs model-name" style="left:100px">IVY</div>
  <div class="abs model-stats" style="left:100px">20 - 5'3 - 120 - 34B</div>

  <div class="abs model-photo" style="left:443px;background:linear-gradient(180deg,#efeeec,#e2dcd6)" role="img" aria-label="Blonde model portrait"></div>
  <div class="abs model-name" style="left:443px">LANA</div>
  <div class="abs model-stats" style="left:443px">23 - 5'0 - 110 - 34C</div>

  <div class="abs model-photo" style="left:785px;background:linear-gradient(160deg,#e6e2de,#8a6b5c 60%,#c9bdb4)" role="img" aria-label="Brunette model portrait with necklace"></div>
  <div class="abs model-name" style="left:785px">CELESTE VANE</div>
  <div class="abs model-stats" style="left:785px">23 - 5'6 - 110 - 32B</div>
</section>

<section>
  <div class="abs testimonials"></div>
  <h2 class="abs section-title testi-title">TESTIMONIALS</h2>
  <div class="abs rule" style="left:540px;top:1412px;width:120px"></div>
  <div class="abs quote-mark" style="left:170px;top:1430px">&ldquo;</div>
  <p class="abs testi-text">VerandaModels Escorts Agency that offers the best companionship &nbsp;in the Miami, Fort Lauderdale, &amp; West Palm Beach areas. Whether you are looking for companions/call girls for a business meeting or if you are just visiting the South Florida area for a short period of time, contact and you will get the best companions that will surely make your time here special and memorable! Click Here to See Our Models!</p>
  <div class="abs quote-mark" style="left:974px;top:1500px">&rdquo;</div>
  <div class="abs avatar" role="img" aria-label="Client photo"></div>
  <div class="abs testi-name">NORA BELLE - CITY NAME</div>
  <div class="abs dots" style="left:571px;top:1679px"><span class="rdot"></span><span class="rdot on"></span><span class="rdot on"></span></div>
</section>

<section>
  <h2 class="abs section-title video-title">OUR VIDEO</h2>
  <div class="abs rule" style="left:535px;top:1845px;width:130px"></div>
  <div class="abs video-text">
    <p>At VerandaModels Escorts, you will come across highly appealing, beautiful, and intelligent escorts. Our South Florida Service portfolio of girls includes the towns best fashion models, hot college girls, girls next door, independent working women etc., to serve all the gentlemen with excellent standards.</p>
    <p>Our companions have to go through a screening process to be a part of our organization as we choose them with the utmost care. All of our girls are properly trained and disciplined and available for any and all types of engagements.</p>
  </div>
  <div class="abs more-btn">MORE INFORMATION <svg width="8" height="12" viewBox="0 0 8 12"><path d="M2 1l4 5-4 5" fill="none" stroke="#cf1f2a" stroke-width="1.6"/></svg></div>
  <div class="abs video-frame">
    <div class="video-still" role="img" aria-label="Video still of a model on the beach">
      <svg style="position:absolute;left:171px;top:70px" width="72" height="72" viewBox="0 0 72 72" aria-hidden="true"><circle cx="36" cy="36" r="33" fill="none" stroke="#fff" stroke-width="3"/><path d="M28 22l22 14-22 14z" fill="none" stroke="#fff" stroke-width="3"/></svg>
      <div class="video-bar">
        <svg width="413" height="28" viewBox="0 0 413 28" aria-hidden="true"><path d="M12 9l9 5-9 5z" fill="#fff"/><rect x="32" y="12" width="285" height="4" rx="2" fill="#888"/><rect x="32" y="12" width="110" height="4" rx="2" fill="#4a9ad6"/><path d="M383 11h4l5-4v14l-5-4h-4z" fill="#fff"/><path d="M395 10c2 2 2 6 0 8" stroke="#fff" stroke-width="1.5" fill="none"/></svg>
      </div>
    </div>
  </div>
</section>

<footer>
  <div class="abs footer"></div>
  <div class="abs foot-head" style="left:100px;top:2284px">Quick Links</div>
  <div class="abs" style="left:100px;top:2339px">
    <div class="foot-link">Home</div><div class="foot-link">Bookings</div><div class="foot-link">Rates</div><div class="foot-link">Models</div>
  </div>
  <div class="abs" style="left:287px;top:2339px">
    <div class="foot-link">Employment</div><div class="foot-link">Links</div><div class="foot-link">Terms of Use</div>
  </div>
  <div class="abs foot-divider" style="left:422px;top:2280px"></div>
  <div class="abs foot-head" style="left:478px;top:2284px">Contact Us</div>
  <div class="abs" style="left:478px;top:2326px">
    <div class="foot-contact">Veranda Models, Street Name,</div>
    <div class="foot-contact">City Address, Country, Pin Code.</div>
    <div class="foot-strong" style="margin-top:8px"><svg width="16" height="16" viewBox="0 0 16 16" aria-hidden="true"><path d="M3 1.5c.8-.6 1.6-.4 2 .4l1 1.7c.3.6.1 1.3-.4 1.7l-.6.5c.5 1.3 1.5 2.4 2.9 3l.5-.6c.4-.6 1.1-.7 1.7-.4l1.7 1c.8.5 1 1.4.3 2.1-1 1.1-2.4 1.4-3.9.7C5.5 10.4 3.6 8.4 2.4 5.7 1.8 4.2 2 2.7 3 1.5z" fill="#fff"/></svg>555-014-2876</div>
    <div class="foot-strong"><svg width="16" height="12" viewBox="0 0 16 12" aria-hidden="true"><rect width="16" height="12" fill="#fff"/><path d="M0 0l8 6 8-6" fill="none" stroke="#cf1f2a" stroke-width="1.4"/></svg>hello@VerandaModels.com</div>
  </div>
  <div class="abs foot-divider" style="left:748px;top:2280px"></div>
  <div class="abs foot-head" style="left:788px;top:2284px">Join Newsletters</div>
  <div class="abs signup"><span class="signup-field">EMAIL ADDRESS</span><span class="signup-btn">SUBSCRIBE</span></div>
  <div class="abs" style="left:788px;top:2388px;display:flex;gap:11px">
    <span class="social"></span><span class="social"></span><span class="social"></span><span class="social"></span><span class="social"></span>
  </div>
  <div class="abs bottombar">&copy; 2017 Veranda Models. &nbsp;All right reserved. &nbsp;Term of Use</div>
</footer>

</body>
</html>
```